Design and Renovation Company Luxury Business Card

I want to create a luxury business card for a Design and Renovation Firm . We will use our current logo. The company name is 742BUILD. We do not want anything standard. We need a very unique concept.
Please see uploaded inspiration. I really like the textured paper option. I would like the card to be thick with debossing, and/or embossing options. The logo has orange in it but I would like to see the card with and without the orange. I think the orange may make the company feel less high-end. The goal is to elevate the logo not match its vibe per se of the logo. We want something very unique, not standard at all!
I would like a space for :
Logo,
Name,
Position,
Email,
Office number,
Website Address,
Business Address,
Thank you!
Have fun!
Target Market(s)
Home owners Age 35 +
Industry/Entity Type
Design and Renovation
Contact Information for Business Card
Logo, Name, Position, Email, Office number, Website Address, Business Address,.
Colors
Designer to choose colors to be used in the design.
Requirements
Must have
- A luxury designer feel. Must be black or dark grey but open to other luxury ideas.
Nice to have
- Gold, silver, black embossing or debossing. Textured paper design.
Should not have
- A cheap look and feel.

```html
<!DOCTYPE html>
<html lang="en">
<head>
<meta charset="utf-8">
<title>742BUILD Business Card</title>
<link rel="stylesheet" href="https://fonts.googleapis.com/css2?family=Questrial&display=swap">
<style>
  :root {
    --backdrop: #3a3a3c;
    --card: #2e3033;
    --card-edge: #26282b;
    --gold: #b8933f;
    --ink-light: #d6d7d9;
  }
  html, body {
    margin: 0;
    padding: 0;
    width: 801px;
    height: 1200px;
    overflow: hidden;
    background: var(--backdrop);
    font-family: "Questrial", "Century Gothic", sans-serif;
  }
  .canvas {
    position: relative;
    width: 801px;
    height: 1200px;
  }
  .card {
    position: absolute;
    left: 90px;
    width: 620px;
    height: 354px;
    background: var(--card);
    border: 1px solid var(--card-edge);
    box-shadow: 0 10px 30px rgba(0,0,0,0.45);
    box-sizing: border-box;
    overflow: hidden;
  }
  .card--front { top: 123px; }
  .card--back { top: 723px; }

  /* Front */
  .front-brand {
    position: absolute;
    left: 250px;
    top: 200px;
    color: var(--gold);
  }
  .front-brand__row {
    display: flex;
    align-items: center;
    gap: 14px;
  }
  .brand-square {
    width: 34px;
    height: 34px;
    background: var(--gold);
  }
  .front-brand__name {
    font-size: 50px;
    letter-spacing: 5px;
    line-height: 1;
  }
  .front-brand__tagline {
    margin-top: 6px;
    font-size: 15px;
    letter-spacing: 3px;
  }

  /* Back */
  .back-brand {
    position: absolute;
    left: 36px;
    top: 150px;
    display: flex;
    flex-direction: column;
    gap: 10px;
    color: var(--gold);
  }
  .back-brand .brand-square {
    width: 44px;
    height: 44px;
  }
  .back-brand__name {
    font-size: 20px;
    letter-spacing: 2px;
  }
  .contact {
    position: absolute;
    left: 350px;
    top: 34px;
    color: var(--ink-light);
    font-size: 18px;
    line-height: 1.3;
  }
  .contact__name {
    margin: 0;
    font-size: 19px;
    font-weight: normal;
    letter-spacing: 1px;
    text-transform: uppercase;
  }
  .contact__role {
    margin: 0 0 58px;
    font-style: italic;
  }
  .contact__lines {
    margin: 0 0 14px;
    padding: 0;
    list-style: none;
  }
  .contact__label {
    display: inline-block;
    width: 24px;
  }
  .contact__address {
    font-style: normal;
  }
</style>
</head>
<body>
<main class="canvas">
  <section class="card card--front" aria-label="Card front">
    <div class="front-brand">
      <div class="front-brand__row">
        <span class="brand-square" aria-hidden="true"></span>
        <span class="front-brand__name">742BUILD</span>
      </div>
      <div class="front-brand__tagline">Design and Renovation Firm</div>
    </div>
  </section>

  <section class="card card--back" aria-label="Card back">
    <div class="back-brand">
      <span class="brand-square" aria-hidden="true"></span>
      <span class="back-brand__name">742BUILD</span>
    </div>
    <div class="contact">
      <h1 class="contact__name">Daniel Ashcombe</h1>
      <p class="contact__role">managing director</p>
      <ul class="contact__lines">
        <li><span class="contact__label">P</span>555 0142 7788</li>
        <li><span class="contact__label">E</span>info@742build.com</li>
        <li><span class="contact__label">W</span>www.742build.com</li>
      </ul>
      <address class="contact__address">48 Alder Lane<br>Brookfield, New York 12345</address>
    </div>
  </section>
</main>
</body>
</html>
```